Quorbanil Business Cards & Stationery Design
Business Cards & Stationery Design
Quorbanil Business Cards & Stationery Design - Information Technology
Creative Brief
Professional
Neville Prothick
Technical Consultant
47 marbury close fenwick NSW 2012 Australia
nprothick@quorbanil.example
http://www.quorbanil.example
The font used is called Aller, and can be downloaded from : http://www.glyphmerrow.example/buyonline/fonts/aller
www.quorbanil.example

```html
<!DOCTYPE html>
<html lang="en">
<head>
<meta charset="utf-8">
<title>Quorbanil Stationery</title>
<link href="https://fonts.googleapis.com/css2?family=Ubuntu:wght@400;500&display=swap" rel="stylesheet">
<style>
  :root{
    --board:#3b3b3b;
    --paper:#ffffff;
    --paper-shade:#eeeeee;
    --ink:#2a2a2a;
    --muted:#8a8a8a;
    --green:#1f7a2e;
    --green-dark:#155a21;
    --band:#1c1c1c;
    --label:#bdbdbd;
  }
  *{margin:0;padding:0;box-sizing:border-box}
  html,body{width:1200px;height:338px;overflow:hidden}
  body{background:var(--board);font-family:'Ubuntu',sans-serif;position:relative}
  .piece{position:absolute;background:var(--paper);overflow:hidden;box-shadow:0 1px 3px rgba(0,0,0,.5)}
  .label{position:absolute;font-size:4px;color:var(--label);white-space:nowrap}
  .wordmark{display:flex;flex-direction:column;align-items:flex-start;color:var(--green);font-weight:500;line-height:1}
  .wordmark .dot{width:5px;height:5px;background:var(--green);margin:0 0 2px 10px}
  .band-top,.band-bottom{position:absolute;left:0;right:0;height:4px;background:var(--band);border-bottom:1px solid var(--green)}
  .band-top{top:0}
  .band-bottom{bottom:0;border-bottom:none;border-top:1px solid var(--green)}
  .faint-name{position:absolute;color:var(--paper-shade);font-weight:500;font-size:34px;white-space:nowrap}
  .tiny{font-size:3px;color:var(--muted);line-height:1.4;position:absolute}

  /* business cards */
  .card{width:70px;height:40px}
  .card-front{left:31px;top:124px}
  .card-back{left:31px;top:180px;background:var(--paper)}
  .card .wordmark{position:absolute;left:6px;top:7px;font-size:8px}
  .card-back .wordmark{left:22px;top:13px}

  /* letterheads */
  .letterhead{width:240px;height:306px;top:18px}
  .letterhead-one{left:120px}
  .letterhead-two{left:384px}
  .letterhead .wordmark{position:absolute;left:24px;top:12px;font-size:13px}
  .letterhead .faint-name{left:46px;top:130px}

  /* compliment slips */
  .slip{width:192px;height:110px;left:629px}
  .slip-front{top:43px}
  .slip-back{top:180px}
  .slip .wordmark{position:absolute;left:14px;top:14px;font-size:12px}

  /* envelopes */
  .envelope{width:336px;left:840px}
  .env-back-dark{top:31px;height:46px;background:var(--paper)}
  .env-back-green{top:80px;height:44px;background:var(--paper)}
  .env-front{top:166px;height:68px}
  .env-front .band-top{height:3px}
  .envelope svg{position:absolute;left:0;top:0}
  .env-front .wordmark{position:absolute;left:10px;top:8px;font-size:6px}
</style>
</head>
<body>

  <!-- business cards -->
  <div class="piece card card-front">
    <div class="wordmark"><span class="dot"></span>quorbanil</div>
    <p class="tiny" style="left:6px;top:24px">Neville Prothick<br>Technical Consultant<br>nprothick@quorbanil.example</p>
  </div>
  <p class="label" style="left:31px;top:117px">Business Card Front</p>

  <div class="piece card card-back">
    <div class="band-top"></div>
    <div class="wordmark"><span class="dot"></span>quorbanil</div>
  </div>
  <p class="label" style="left:31px;top:173px">Business Card Back</p>

  <!-- letterheads -->
  <div class="piece letterhead letterhead-one">
    <div class="band-top"></div>
    <div class="wordmark"><span class="dot"></span>quorbanil</div>
    <p class="tiny" style="left:24px;top:46px">47 marbury close fenwick NSW 2012 Australia</p>
    <div class="faint-name">quorbanil</div>
    <p class="tiny" style="left:24px;top:262px">nprothick@quorbanil.example<br>http://www.quorbanil.example</p>
    <div class="band-bottom"></div>
  </div>
  <p class="label" style="left:200px;top:327px">Letterhead Page 1</p>

  <div class="piece letterhead letterhead-two">
    <div class="band-top"></div>
    <div class="faint-name">quorbanil</div>
    <p class="tiny" style="left:60px;top:290px">47 marbury close fenwick NSW 2012 Australia · www.quorbanil.example</p>
    <div class="band-bottom"></div>
  </div>
  <p class="label" style="left:468px;top:327px">Letterhead Page 2</p>

  <!-- compliment slips -->
  <div class="piece slip slip-front">
    <div class="band-top"></div>
    <div class="wordmark"><span class="dot"></span>quorbanil</div>
    <p class="tiny" style="left:14px;top:36px">47 marbury close fenwick NSW 2012 Australia</p>
    <div class="band-bottom"></div>
  </div>
  <p class="label" style="left:700px;top:170px">Comp Slip Front</p>

  <div class="piece slip slip-back">
    <div class="band-top"></div>
    <div class="wordmark"><span class="dot"></span>quorbanil</div>
    <div class="band-bottom"></div>
  </div>
  <p class="label" style="left:700px;top:292px">Comp Slip Back</p>

  <!-- envelopes -->
  <div class="piece envelope env-back-dark">
    <svg width="336" height="46" viewBox="0 0 336 46" aria-hidden="true">
      <path d="M0 0 H336 V8 Q168 52 0 8 Z" fill="#1c1c1c"/>
      <path d="M0 8 Q168 52 336 8" fill="none" stroke="#1f7a2e" stroke-width="1"/>
      <rect x="165" y="14" width="6" height="6" fill="#1f7a2e"/>
    </svg>
  </div>
  <div class="piece envelope env-back-green">
    <svg width="336" height="44" viewBox="0 0 336 44" aria-hidden="true">
      <path d="M0 0 H336 V8 Q168 50 0 8 Z" fill="#1f7a2e"/>
      <rect x="165" y="12" width="6" height="6" fill="#ffffff"/>
      <path d="M0 44 L150 26 H186 L336 44" fill="none" stroke="#dddddd" stroke-width="1"/>
    </svg>
  </div>
  <div class="piece envelope env-front">
    <div class="band-top"></div>
    <div class="wordmark"><span class="dot"></span>quorbanil</div>
    <p class="tiny" style="left:10px;top:24px">47 marbury close fenwick NSW 2012 Australia</p>
  </div>
  <p class="label" style="left:960px;top:240px">Envelope Back and Front</p>

</body>
</html>
```